Drumm's Accord business card design

I am a private mediator and family dispute resolution practitioner. I am located on Gold Coast, Australia. Private mediation is mandatory within the Household Relations Code so I offer very affordable private mediation for families and workplace and community. We also offer education and workshops training and development for schools, families and businesses based on becoming more open and effective communicator and anti conflict resolution, dispute resolution. We facilitate crucial conversations and help families create parenting agreements/plans about their children and situation and people to live in harmony even though they may disagree. We would like to see designs that are simple that use vibrant pink/purple, poppy red and vibrant blue (colour of communication) or yellow or vibrant lime green. We would like the design represent new growth, moving forward in separate ways but harmony similar to a seed (circle open at the top) with new shoots in opposite direction. The final design should communicate moving forward in slightly different ways with the principle from family represented by seed or something similar.

Drumm's Accord, Helen Drumm,PO Box 152, Robina Qld 4226Effective Private Mediation, Anti Conflict Coaching, Couples and individual coaching. family | workplace | community Competitive rates | after hour appointments. Nationally Accredited Mediator, Family Dispute Resolution Practitioner M: 0427518260 E: helendrumm4@quellmail.com

Sans Serif

a64599
fbed22
ec1f27
fff5ef

Must have
• colour and be double sided
• vibrant poppy colour red is my preference blended or contrasted with purple or other contrast colour
• elegant professional font cannot add file for some reason below under image or sketch but google images have good variety of red/orange colour of poppy flower that I like
Nice to have
• graduated colour from left to right
Should not have
• no capital/ block text that look solid or chunky

```html
<!DOCTYPE html>
<html lang="en">
<head>
<meta charset="utf-8">
<title>Drumm's Accord – Business Card</title>
<link rel="stylesheet" href="https://fonts.googleapis.com/css2?family=Montserrat:wght@400;500&family=Fira+Sans:wght@400;500&display=swap">
<style>
  :root {
    --stage: #1b1b1c;
    --card-light: #f4f4f4;
    --card-light-edge: #dcdcdc;
    --ink-grey: #4a4a4c;
    --card-dark: #050505;
    --steel-light: #9c9c9e;
    --steel-dark: #2b2b2c;
    --poppy: #ec1f27;
    --violet: #a64599;
    --violet-soft: #c47bbb;
    --white: #f4f4f4;
  }
  * { margin: 0; padding: 0; box-sizing: border-box; }
  html, body {
    width: 1200px; height: 871px; overflow: hidden;
    background: var(--stage);
  }
  .stage { position: relative; width: 1200px; height: 871px; }

  .card {
    position: absolute;
    width: 600px; height: 343px;
    border-radius: 4px;
    overflow: hidden;
  }

  /* Front */
  .card--front {
    left: 70px; top: 80px;
    background: linear-gradient(135deg, var(--card-light) 0%, var(--card-light-edge) 100%);
    display: flex; flex-direction: column; align-items: center; justify-content: center;
  }
  .brand { display: flex; align-items: center; gap: 16px; }
  .brand__mark {
    width: 30px; height: 30px; border-radius: 50%;
    background: var(--poppy);
  }
  .brand__name {
    font-family: 'Montserrat', sans-serif; font-weight: 500;
    letter-spacing: 1.5px;
  }
  .card--front .brand__name { font-size: 38px; color: var(--ink-grey); }
  .services {
    margin-top: 22px;
    font-family: 'Montserrat', sans-serif; font-weight: 400;
    font-size: 15px; letter-spacing: 0.5px; line-height: 1.5;
    color: var(--ink-grey); text-align: center;
  }
  .services__sep { color: var(--poppy); padding: 0 4px; }

  /* Back */
  .card--back {
    left: 530px; top: 448px;
    background: var(--card-dark);
  }
  .back__panel {
    position: absolute; left: 0; top: 0; bottom: 0; width: 250px;
    background: linear-gradient(100deg, var(--steel-light) 0%, var(--steel-dark) 75%, var(--card-dark) 100%);
    display: flex; flex-direction: column; align-items: center; justify-content: center;
  }
  .card--back .brand { flex-direction: column; gap: 14px; }
  .card--back .brand__mark { width: 26px; height: 26px; }
  .card--back .brand__name { font-size: 23px; color: var(--white); letter-spacing: 1px; }
  .back__divider {
    position: absolute; left: 272px; top: 40px; width: 2px; height: 190px;
    background: linear-gradient(180deg, var(--poppy) 0%, var(--violet) 100%);
  }
  .contact { position: absolute; left: 300px; top: 46px; right: 16px; }
  .contact__name {
    font-family: 'Montserrat', sans-serif; font-weight: 500;
    font-size: 27px; letter-spacing: 1px; color: var(--white);
  }
  .contact__role {
    margin-top: 8px;
    font-family: 'Fira Sans', sans-serif; font-weight: 500;
    font-size: 13.5px; line-height: 1.4; color: var(--violet-soft); letter-spacing: 0.3px;
  }
  .contact__list { list-style: none; margin-top: 12px; }
  .contact__item {
    display: flex; align-items: center; gap: 14px;
    font-family: 'Montserrat', sans-serif; font-weight: 400;
    font-size: 14px; letter-spacing: 0.3px; color: var(--white);
    margin-bottom: 9px;
  }
  .contact__item svg { width: 14px; height: 14px; flex: none; fill: var(--poppy); }
  .back__band {
    position: absolute; left: 265px; right: 0; bottom: 0; height: 24px;
    background: linear-gradient(90deg, var(--poppy) 0%, var(--violet) 100%);
  }
</style>
</head>
<body>
<main class="stage">
  <section class="card card--front" aria-label="Card front">
    <div class="brand">
      <span class="brand__mark"></span>
      <span class="brand__name">Drumm's Accord</span>
    </div>
    <p class="services">Effective Private Mediation<span class="services__sep">|</span>Anti Conflict Coaching<br>Couples and Individual Coaching</p>
  </section>

  <section class="card card--back" aria-label="Card back">
    <div class="back__panel">
      <div class="brand">
        <span class="brand__mark"></span>
        <span class="brand__name">Drumm's Accord</span>
      </div>
    </div>
    <div class="back__divider"></div>
    <div class="contact">
      <h1 class="contact__name">Helen Drumm</h1>
      <p class="contact__role">Nationally accredited Mediator,<br>Family Dispute Resolution Practitioner</p>
      <ul class="contact__list">
        <li class="contact__item">
          <svg viewBox="0 0 24 24"><path d="M12 2a7 7 0 0 0-7 7c0 5 7 13 7 13s7-8 7-13a7 7 0 0 0-7-7zm0 9.5A2.5 2.5 0 1 1 12 6.5a2.5 2.5 0 0 1 0 5z"/></svg>
          PO Box 367, Varndale Qld 4295
        </li>
        <li class="contact__item">
          <svg viewBox="0 0 24 24"><path d="M7 1h10a2 2 0 0 1 2 2v18a2 2 0 0 1-2 2H7a2 2 0 0 1-2-2V3a2 2 0 0 1 2-2zm0 3v14h10V4z"/></svg>
          0427518260
        </li>
        <li class="contact__item">
          <svg viewBox="0 0 24 24"><path d="M2 5h20v14H2zm2 2v.5l8 5 8-5V7z"/></svg>
          helendrumm4@quellmail.com
        </li>
      </ul>
    </div>
    <div class="back__band"></div>
  </section>
</main>
</body>
</html>
```